Quellora business card design

create modern and tech looking business card that is clean but effectively communciates that we are a cloud communications company.
Should have at minimum:
Employee Name
Postion
Phone Number
Email
website
Contact Information for Business Card
create modern and tech looking business card that is clean but effectively communciates that we are a cloud communications company. We have two logo color schemes (attached) so would like to see designs both ways
Should have at minimum:
Employee Name
Postion
Phone Number
Email
website

```html
<!DOCTYPE html>
<html lang="en">
<head>
<meta charset="utf-8">
<title>Quellora Business Card</title>
<link href="https://fonts.googleapis.com/css2?family=Roboto:wght@400;500;700&display=swap" rel="stylesheet">
<style>
  :root {
    --stage: #c9c9c9;
    --cyan: #2cb1d4;
    --violet: #562279;
    --violet-mid: #4a5ea3;
    --paper: #f2f2f2;
    --ink: #4a4a4a;
    --ink-soft: #3a3a3a;
    --white: #ffffff;
  }
  * { margin: 0; padding: 0; box-sizing: border-box; }
  html, body {
    width: 1200px; height: 576px; overflow: hidden;
    background: var(--stage);
    font-family: "Roboto", Arial, sans-serif;
  }
  .canvas { position: relative; width: 1200px; height: 576px; }

  .card {
    position: absolute; top: 140px;
    width: 484px; height: 292px;
    border-radius: 14px; overflow: hidden;
    box-shadow: 0 4px 10px rgba(0,0,0,0.25);
  }

  /* Front */
  .card-front {
    left: 82px;
    background: linear-gradient(180deg, var(--cyan) 0%, var(--violet-mid) 50%, var(--violet) 100%);
    display: flex; align-items: center; justify-content: center; gap: 14px;
  }
  .brand-mark {
    width: 22px; height: 22px; background: var(--white);
  }
  .brand-name-front {
    color: var(--white); font-weight: 500; font-size: 40px; letter-spacing: 2px;
  }

  /* Back */
  .card-back { left: 602px; background: var(--paper); }
  .card-back .waves { position: absolute; inset: 0; }
  .corner-pattern {
    position: absolute; top: 0; right: 0; width: 80px; height: 76px;
    background: linear-gradient(225deg, rgba(86,34,121,0.35), rgba(44,177,212,0.25) 55%, rgba(242,242,242,0) 85%);
  }
  .brand-back {
    position: absolute; left: 24px; top: 52px;
    display: flex; align-items: center; gap: 12px;
  }
  .brand-back .brand-mark { background: var(--violet); width: 20px; height: 20px; }
  .brand-name-back {
    color: var(--ink); font-weight: 500; font-size: 32px; letter-spacing: 1.5px;
  }
  .person { position: absolute; left: 42px; top: 158px; }
  .person-name { color: var(--violet); font-weight: 700; font-size: 22px; }
  .person-role { color: var(--ink-soft); font-size: 12px; margin-top: 6px; }

  .contacts {
    position: absolute; right: 20px; top: 213px;
    list-style: none; text-align: right;
  }
  .contacts li {
    color: var(--white); font-size: 12px; line-height: 18px;
    display: flex; align-items: center; justify-content: flex-end; gap: 8px;
  }
  .contacts svg { width: 11px; height: 11px; fill: var(--white); }
</style>
</head>
<body>
<div class="canvas">

  <section class="card card-front">
    <span class="brand-mark"></span>
    <span class="brand-name-front">QUELLORA</span>
  </section>

  <section class="card card-back">
    <svg class="waves" viewBox="0 0 484 292" preserveAspectRatio="none">
      <path fill="var(--violet)" d="M0,252 C110,262 210,240 300,205 C370,178 430,166 484,164 L484,292 L0,292 Z"/>
      <path fill="var(--cyan)" d="M0,216 C90,245 200,240 300,200 C370,172 430,156 484,150 L484,158 C430,164 372,182 306,210 C210,250 100,258 0,238 Z"/>
      <path fill="var(--cyan)" d="M36,236 C140,252 240,232 330,196 C300,216 230,244 150,250 C100,253 60,246 36,236 Z" opacity="0.85"/>
    </svg>
    <div class="corner-pattern" role="img" aria-label="Scattered cyan and violet pixel squares decoration"></div>

    <div class="brand-back">
      <span class="brand-mark"></span>
      <span class="brand-name-back">QUELLORA</span>
    </div>

    <div class="person">
      <div class="person-name">Mara Ellison</div>
      <div class="person-role">Managing Director</div>
    </div>

    <ul class="contacts">
      <li>1800-555-0147
        <svg viewBox="0 0 24 24"><path d="M6.6 10.8a15 15 0 0 0 6.6 6.6l2.2-2.2c.3-.3.7-.4 1-.2 1.1.4 2.3.6 3.6.6.6 0 1 .4 1 1V20c0 .6-.4 1-1 1A17 17 0 0 1 3 4c0-.6.4-1 1-1h3.5c.6 0 1 .4 1 1 0 1.3.2 2.5.6 3.6.1.3 0 .7-.2 1z"/></svg>
      </li>
      <li>www.quellora-cloud.com
        <svg viewBox="0 0 24 24"><path d="M2 5h20v14H2z M2 5l10 8 10-8" fill="none" stroke="#fff" stroke-width="2.5"/></svg>
      </li>
      <li>mara@quellora-cloud.com
        <svg viewBox="0 0 24 24"><circle cx="12" cy="12" r="9" fill="none" stroke="#fff" stroke-width="2.5"/><path d="M3 12h18M12 3c4 4 4 14 0 18M12 3c-4 4-4 14 0 18" fill="none" stroke="#fff" stroke-width="2"/></svg>
      </li>
    </ul>
  </section>

</div>
</body>
</html>
```